Company Website

We require an online clothing store website for construction workwear.
It needs to be easy to read, user friendly, easy to navigate purchasing.
We are after designs incorporating our recently design logo, and colour combinations black white and orange (same as the company logo). Needs to highlight quality, safety and products. Any ideas around highlighting branding are welcome.

Target Market(s)

Construction workers and businesses.

Industry/Entity Type

Construction

Coding

Coded - Design and coding required

Number of Pages Required

5+ page

Colors
EE7325
F08F49
F5BC92
FAE3D3
FDF4ED

Requirements
Must have
• Include all pictures, prices and details of the products we sell. See PDF uploaded to brief.
Nice to have
• Simple access to purchase items. Easy to navigate website layout.

```html
<!DOCTYPE html>
<html lang="en">
<head>
<meta charset="utf-8">
<title>Ironline Workwear</title>
<link href="https://fonts.googleapis.com/css2?family=Montserrat:wght@400;500;600;700;800&display=swap" rel="stylesheet">
<style>
:root{
  --orange:#f25a00;
  --orange-soft:#f08f49;
  --peach:#fae3d3;
  --ink:#111111;
  --dark:#3a3a3a;
  --white:#ffffff;
  --grey:#777777;
}
*{box-sizing:border-box;margin:0;padding:0}
html,body{width:1200px;height:4203px;overflow:hidden}
body{font-family:"Montserrat",sans-serif;color:var(--ink);background:var(--white);position:relative}
.abs{position:absolute}
.btn{position:absolute;background:var(--orange);color:var(--white);font-weight:600;font-size:15px;display:flex;align-items:center;justify-content:center}
.section-title{position:absolute;left:0;width:1200px;text-align:center;font-weight:800;font-size:38px;letter-spacing:.2px}
/* top bar */
.topbar{left:0;top:0;width:1200px;height:46px;background:var(--orange);color:var(--white);font-size:13px}
.topbar .mail{left:112px;top:15px}
.topbar .ship{left:508px;top:15px}
.topbar .social{left:1056px;top:9px;width:28px;height:28px;border-radius:5px;background:var(--white)}
/* nav */
.nav{left:0;top:46px;width:1200px;height:88px;background:var(--white)}
.brand{left:102px;top:14px;color:var(--orange);font-weight:800;font-size:30px;letter-spacing:3px}
.brand small{display:block;font-size:12px;letter-spacing:7px;color:var(--ink);font-weight:600;text-align:right}
.menu{left:532px;top:35px;display:flex;gap:38px;font-size:13px;font-weight:500}
.nav .icon{top:26px;width:32px;height:32px;border-radius:50%;background:var(--orange)}
/* hero */
.hero{left:0;top:134px;width:1200px;height:618px;overflow:hidden}
.hero .photo{position:absolute;inset:0;background:linear-gradient(90deg,#1b2430 0%,#2f3a44 45%,#6f7a3a 70%,#b9b84a 100%)}
.hero h4{left:112px;top:130px;color:var(--white);font-size:24px;font-weight:700}
.hero h1{left:112px;top:160px;color:var(--white);font-size:42px;font-weight:800;line-height:50px}
.hero p{left:112px;top:268px;color:var(--white);font-size:19px;line-height:38px;font-weight:500;white-space:nowrap}
/* categories */
.cat{top:920px;width:353px;height:264px;border:2px solid var(--peach);border-radius:6px;background:var(--white);box-shadow:0 2px 8px rgba(0,0,0,.08)}
.cat h3{position:absolute;left:18px;top:80px;font-size:20px;font-weight:600}
.cat .btn{left:20px;top:132px;width:158px;height:46px}
.cat .pic{position:absolute;right:14px;top:30px;width:150px;height:200px;border-radius:6px}
/* about */
.about{left:0;top:1372px;width:1200px;height:589px;background:linear-gradient(180deg,#3b3b3b,#454545)}
.about .frame{position:absolute;left:125px;top:108px;width:386px;height:324px;border:2px solid var(--orange)}
.about .pic{position:absolute;left:157px;top:132px;width:407px;height:345px;background:linear-gradient(135deg,#6b4a2a,#c9a23a 55%,#3b2a1a)}
.about h2{left:605px;top:88px;color:var(--white);font-size:38px;font-weight:800}
.about p{left:601px;top:150px;width:430px;color:var(--white);font-size:15px;line-height:27.5px}
/* products */
.prod{top:2128px;width:306px;height:482px;background:var(--white);box-shadow:0 2px 10px rgba(0,0,0,.12);border-radius:3px;text-align:center}
.prod .pic{position:absolute;left:6px;top:6px;width:294px;height:226px}
.prod .rating{position:absolute;left:0;top:248px;width:100%;font-size:17px;color:var(--ink)}
.prod .rating span{color:#f5b400;font-size:26px;letter-spacing:1px;vertical-align:-3px}
.prod h3{position:absolute;left:0;top:294px;width:100%;font-size:21px;font-weight:500;line-height:32px}
.prod .price{position:absolute;left:0;top:372px;width:100%;font-size:19px;font-weight:600}
.prod .btn{left:73px;top:412px;width:158px;height:46px}
.arrow{top:2356px;width:42px;height:42px;border-radius:50%}
/* newsletter */
.news{left:0;top:2714px;width:1200px;height:394px;background:linear-gradient(180deg,#3a3a3a,#4a4a4a)}
.news h2{left:0;top:100px;width:1200px;text-align:center;color:var(--white);font-size:38px;font-weight:800}
.news p{left:0;top:176px;width:1200px;text-align:center;color:var(--white);font-size:13.5px}
.news .field{left:186px;top:218px;width:826px;height:52px;background:var(--white);border:2px solid var(--orange)}
.news .field span{position:absolute;left:24px;top:15px;font-size:15px;color:#555}
.news .field .btn{left:642px;top:0;width:180px;height:48px;font-size:16px}
/* gallery */
.gallery{top:3287px;width:245px;height:304px}
/* footer */
.footer{left:0;top:3821px;width:1200px;height:382px;background:#000;color:var(--white)}
.footer .fbrand{left:104px;top:88px;color:var(--orange);font-weight:800;font-size:26px;letter-spacing:2px}
.footer .fbrand small{display:block;font-size:10px;letter-spacing:6px;color:var(--white);text-align:right;font-weight:600}
.footer h4{top:76px;font-size:20px;font-weight:600}
.footer ul{list-style:none;top:130px;font-size:14px;line-height:30px}
.footer .contact li{display:flex;gap:8px;align-items:flex-start}
.card{top:280px;width:60px;height:30px;border-radius:4px;background:var(--white)}
.footer .rule{left:110px;top:330px;width:978px;height:1px;background:var(--white)}
.footer .copy{left:0;top:352px;width:1200px;text-align:center;font-size:13px}
</style>
</head>
<body>

<header class="abs topbar">
  <div class="abs mail">✉ info@ironlinewear.com</div>
  <div class="abs ship">🚚 Free Shipping</div>
  <div class="abs social" aria-label="Social page"></div>
</header>

<nav class="abs nav">
  <div class="abs brand">IRONLINE<small>WORKWEAR</small></div>
  <div class="abs menu"><span>HOME</span><span>PRODUCT</span><span>ABOUT US</span><span>BLOGS</span><span>CONTACT</span></div>
  <div class="abs icon" style="left:1000px">
    <svg width="32" height="32"><circle cx="15" cy="15" r="6" fill="none" stroke="#fff" stroke-width="2"/><line x1="19" y1="19" x2="23" y2="23" stroke="#fff" stroke-width="2"/></svg>
  </div>
  <div class="abs" style="left:1054px;top:28px">
    <svg width="26" height="26"><path d="M2 4h4l3 12h11l3-9H8" fill="none" stroke="#f25a00" stroke-width="2.5"/><circle cx="10" cy="21" r="2" fill="#f25a00"/><circle cx="19" cy="21" r="2" fill="#f25a00"/></svg>
  </div>
</nav>

<section class="abs hero">
  <div class="photo" role="img" aria-label="Two site workers in hard hats and hi-vis jackets reviewing a laptop in a factory"></div>
  <h4 class="abs">WELCOME TO</h4>
  <h1 class="abs">IRONLINE<br>WORKWEAR</h1>
  <p class="abs">Lorem Ipsum is simply dummy text of the<br>printing and typesetting industry. Lorem</p>
  <div class="btn" style="left:112px;top:368px;width:158px;height:46px">Get Started</div>
  <svg class="abs" style="left:0;top:530px" width="1200" height="88">
    <path d="M0 0 L318 58 L1200 0 L1200 88 L0 88 Z" fill="#fff" transform="translate(0,20)"/>
    <path d="M0 14 L318 72 L1200 16 L1200 30 L318 88 L0 26 Z" fill="#f25a00"/>
  </svg>
</section>

<h2 class="section-title" style="top:838px">OUR CATEGORIES</h2>
<article class="abs cat" style="left:39px"><h3>Lorem Ipsum</h3><div class="btn">Shop Now</div><div class="pic" role="img" aria-label="Blue hi-vis work shirt" style="background:linear-gradient(180deg,#2d7fd0,#232a8a)"></div></article>
<article class="abs cat" style="left:426px"><h3>Lorem Ipsum</h3><div class="btn">Shop Now</div><div class="pic" role="img" aria-label="Yellow hard hat" style="background:radial-gradient(circle at 50% 55%,#f4c21a,#e7a70a 55%,#fff 72%)"></div></article>
<article class="abs cat" style="left:812px"><h3>Lorem Ipsum</h3><div class="btn">Shop Now</div><div class="pic" role="img" aria-label="Pair of grey and yellow work gloves" style="background:linear-gradient(90deg,#3c3c3c,#6a6a6a 45%,#f2b516 55%,#e09a10)"></div></article>
<div class="btn" style="left:519px;top:1233px;width:160px;height:46px">View More</div>

<section class="abs about">
  <div class="frame"></div>
  <div class="pic" role="img" aria-label="Safety gear laid out on wooden boards: respirator, goggles, ear defenders, gloves and hard hat"></div>
  <h2 class="abs">ABOUT US</h2>
  <p class="abs">Lorem Ipsum is simply dummy text of the printing and typesetting industry. Lorem Ipsum has been the industry's standard dummy text ever since the 1500s, when an unknown printer took a galley of type and scrambled it to make a type specimen book. It has survived not only five centuries, but also the leap into electronic typesetting, remaining essentially unchanged.It was popularised in the 1960s with the release of Letraset sheets containing Lorem Ipsum</p>
  <div class="btn" style="left:599px;top:431px;width:158px;height:46px">Read More</div>
</section>

<h2 class="section-title" style="top:2043px">OUR PRODUCTS</h2>
<div class="abs arrow" style="left:32px;background:#8a8a8a"><svg width="42" height="42"><path d="M24 13l-8 8 8 8" fill="none" stroke="#fff" stroke-width="3"/></svg></div>
<div class="abs arrow" style="left:1132px;background:var(--orange)"><svg width="42" height="42"><path d="M18 13l8 8-8 8" fill="none" stroke="#fff" stroke-width="3"/></svg></div>
<article class="abs prod" style="left:109px"><div class="pic" role="img" aria-label="Orange and grey work gloves" style="background:linear-gradient(135deg,#f3a642,#4a4a4a)"></div><div class="rating"><span>★★★★★</span> (41)</div><h3>Lorem Ipsum by<br>Lorem Ipsum</h3><div class="price">$25</div><div class="btn">Shop Now</div></article>
<article class="abs prod" style="left:444px"><div class="pic" role="img" aria-label="Yellow hard hat with leather work gloves" style="background:radial-gradient(circle at 45% 45%,#f7cb1b,#e8a50c 55%,#fff 75%)"></div><div class="rating"><span>★★★★★</span> (41)</div><h3>Lorem Ipsum by<br>Lorem Ipsum</h3><div class="price">$25</div><div class="btn">Shop Now</div></article>
<article class="abs prod" style="left:784px"><div class="pic" role="img" aria-label="Red and white ear defenders" style="background:radial-gradient(circle at 50% 50%,#fff,#e9e9e9 40%,#d94b4b 70%,#fff 85%)"></div><div class="rating"><span>★★★★★</span> (41)</div><h3>Lorem Ipsum by<br>Lorem Ipsum</h3><div class="price">$25</div><div class="btn" style="top:408px">Shop Now</div></article>

<section class="abs news">
  <h2 class="abs">SIGN UP TO OUR NEWSLETTER</h2>
  <p class="abs">Lorem Ipsum is simply dummy text of the printing and typesetting industry. Lorem Ipsum has been the</p>
  <div class="abs field"><span>Enter Email Address</span><div class="btn">Subscribe</div></div>
</section>

<h2 class="section-title" style="top:3208px">OUR GALLERY</h2>
<div class="abs gallery" style="left:106px;background:linear-gradient(160deg,#c9a25a,#6b4a2e)" role="img" aria-label="Carpenter in a yellow hard hat at work"></div>
<div class="abs gallery" style="left:351px;background:linear-gradient(160deg,#e5b31c,#7a5a32)" role="img" aria-label="Safety gear on wooden boards"></div>
<div class="abs gallery" style="left:596px;background:linear-gradient(160deg,#8a9a6a,#e57a1e 60%,#2a2a2a)" role="img" aria-label="Forestry worker in orange protective jacket and helmet"></div>
<div class="abs gallery" style="left:840px;width:244px;background:linear-gradient(160deg,#3a3a3a,#9a7a5a)" role="img" aria-label="Close-up of brown leather work boots"></div>
<div class="btn" style="left:519px;top:3638px;width:158px;height:46px">View More</div>

<svg class="abs" style="left:0;top:3736px" width="1200" height="90">
  <path d="M0 72 L882 4 L1200 68 L1200 90 L0 90 Z" fill="#000"/>
  <path d="M0 72 L882 0 L1200 62 L1200 72 L882 20 L0 80 Z" fill="#f25a00"/>
</svg>
<footer class="abs footer">
  <div class="abs fbrand">IRONLINE<small>WORKWEAR</small></div>
  <h4 class="abs" style="left:400px">Main Links</h4>
  <ul class="abs" style="left:403px"><li>Home</li><li>Product</li><li>About Us</li><li>Blogs</li><li>Contact</li></ul>
  <h4 class="abs" style="left:633px">Other Links</h4>
  <ul class="abs" style="left:636px"><li>Privacy Policy</li><li>Terms and Condition</li><li>Legal information</li></ul>
  <h4 class="abs" style="left:885px">Contact Details</h4>
  <ul class="abs contact" style="left:883px;width:200px;line-height:28px">
    <li><span>✆</span><span>+1 555 014 2290</span></li>
    <li><span>✉</span><span>admin@ ironlinewear.com</span></li>
    <li><span>⌖</span><span>Lorem Ipsum, Lorem, Lorem, ipsum</span></li>
  </ul>
  <div class="abs card" style="left:110px"></div>
  <div class="abs card" style="left:184px"></div>
  <div class="abs card" style="left:258px"></div>
  <div class="abs rule"></div>
  <div class="abs copy">© 2024 &nbsp; Ironline Workwear &nbsp;| All Rights Reserved</div>
</footer>

</body>
</html>
```